Online-Marketing Material für Nähmaschinen
Es wurde alles gut umgesetzt und der Kontakt war sehr freundlich und zuverlässig. Danke.
Zielgruppe
Wir verkaufen Nähmaschinen, Stickmaschinen, Overlock und Nähzubehör über unseren Laden und Onlineshop www.Fadenwelt-Haendler.de
Unsere Zielgruppe sind zu 95% Frauen im Alter von 20 - 65 Jahren.
Aufgabenstellung
Wir möchten gerne einen Werbebanner (Bannergröße 2320x540 Pixel) zum Black Friday für unsere Startseite im Onlineshop und Angebotsbilder zu gewissen Maschinen. Bezüglich den Angebotsbilder. Hier sollte bitte eine Umrandung erstellt werden, die wir dann um die Bilder legen können im Photoshop. Der Banner sollte folgendes enthalten.
- WILDE STOFF TAGE (statt Black Friday)
- bis zu 40% sparen
- gültig von 21. - 28.11.2022
Ich habe auch noch unser Firmenlogo und Bilder von Maschinen mit angehängt, die eingebaut werden könnten.
Es ist auch ein alter WILDE STOFF TAGE Banner als Vorlage in welche Richtung es gehen könnte.
Allerdings sind wir an etwas neuem sehr offen.
Viele Grüße
Matthias Lenhart

```html
<!DOCTYPE html>
<html lang="de">
<head>
<meta charset="utf-8">
<title>Fadenwelt Händler – Startseite</title>
<link href="https://fonts.googleapis.com/css2?family=Bebas+Neue&family=Open+Sans:wght@400;600;700&display=swap" rel="stylesheet">
<style>
:root{
  --red:#d2131d;
  --dark:#333;
  --header:#f5f5f5;
  --text:#4b5a69;
  --line:#dadae5;
  --banner-dark:#1a1212;
  --banner-mid:#4a1414;
}
*{margin:0;padding:0;box-sizing:border-box}
html,body{width:1200px;height:656px;overflow:hidden;background:#fff;font-family:"Open Sans",sans-serif;color:var(--dark)}
.page{position:relative;width:1200px;height:656px}
.topbar{position:absolute;left:0;top:0;width:1200px;height:16px;background:var(--dark);color:#fff;font-size:7px}
.topbar span{position:absolute;top:3px}
.topbar .ico{width:14px;height:9px;border-radius:2px;background:#ccc;top:3px}
.header{position:absolute;left:0;top:16px;width:1200px;height:100px;background:var(--header)}
.about{position:absolute;left:934px;top:5px;font-size:9px;color:#555}
.logo{position:absolute;left:213px;top:30px;display:flex;align-items:center;gap:8px}
.logo-name{font-weight:700;font-size:17px;line-height:17px;color:var(--red);letter-spacing:.5px}
.logo-mark{width:22px;height:22px;background:var(--red)}
.badge{position:absolute;border-radius:50%}
.search{position:absolute;left:768px;top:32px;width:220px;height:24px;background:#fff;border:1px solid var(--line);border-radius:2px;font-size:9px;color:#aaa;padding:5px 6px}
.search svg{position:absolute;right:6px;top:5px}
.btn{position:absolute;top:69px;height:25px;background:#fff;border:1px solid var(--line);border-radius:2px;font-size:9px;color:#555;display:flex;align-items:center;justify-content:center;gap:5px}
.nav{position:absolute;left:0;top:116px;width:1200px;height:26px;background:#fff;font-size:10.5px;color:#555}
.nav span{position:absolute;top:6px}
.nav .home{left:206px;top:0;width:47px;height:26px;background:var(--red);color:#fff;font-weight:700;padding-top:6px;text-align:center}
.hero{position:absolute;left:0;top:142px;width:1200px;height:280px;overflow:hidden;
  background:linear-gradient(120deg,var(--banner-dark) 0%,var(--banner-mid) 30%,#200e0e 45%,var(--banner-mid) 60%,#150d0d 80%,#2a1010 100%)}
.hero-title{position:absolute;left:58px;top:30px;font-family:"Bebas Neue",sans-serif;font-size:134px;line-height:134px;color:#fff;letter-spacing:3px;white-space:nowrap}
.hero-date{position:absolute;left:430px;top:174px;width:408px;height:64px;background:#fff;color:var(--red);font-family:"Bebas Neue",sans-serif;font-size:46px;line-height:66px;text-align:center}
.ribbon{position:absolute;left:920px;top:0}
.intro{position:absolute;left:0;top:470px;width:1200px;text-align:center}
.intro h1{font-size:16.5px;font-weight:700;color:var(--dark)}
.intro p{margin:10px auto 0;width:740px;font-size:8.6px;line-height:15px;color:var(--text)}
.tile{position:absolute;top:552px;height:62px;overflow:hidden}
.tile-label{position:absolute;top:18px;height:26px;background:#fff;color:var(--red);font-weight:700;font-size:17.5px;letter-spacing:.5px;text-align:center;line-height:26px}
.cookie{position:absolute;left:0;top:614px;width:1200px;height:42px;background:#fff;border-top:1px solid #eee;font-size:8.6px;color:#555;line-height:12px}
.cookie p{position:absolute;left:14px;top:7px;width:940px}
.cookie a{color:var(--red);text-decoration:none}
.cbtn{position:absolute;top:14px;height:25px;border:1px solid var(--line);border-radius:2px;font-size:8.6px;font-weight:700;color:#555;text-align:center;line-height:23px;background:#fff}
.cbtn.primary{background:var(--red);color:#fff;border-color:var(--red)}
.trust{position:absolute;left:1129px;top:535px;width:59px;height:96px;background:#fff;border-radius:5px;box-shadow:0 0 6px rgba(0,0,0,.18);text-align:center;font-size:7.5px;color:#111}
.trust .seal{width:30px;height:30px;border-radius:50%;background:#f0c24a;border:3px solid #444;margin:8px auto 4px}
.stars{color:#f4b400;font-size:8px;letter-spacing:1px}
</style>
</head>
<body>
<div class="page">

  <div class="topbar">
    <i class="ico" style="position:absolute;left:290px"></i><span style="left:320px">0 % Finanzierung**</span>
    <i class="ico" style="position:absolute;left:416px"></i><span style="left:446px">Versandkostenfrei ab 25,- € Bestellwert</span>
    <svg style="position:absolute;left:606px;top:2px" width="12" height="12" viewBox="0 0 24 24"><path d="M6 2l4 4-2 3c1 3 4 6 7 7l3-2 4 4-3 4C10 22 2 14 2 5z" fill="#ccc"/></svg>
    <span style="left:636px">08512 - 4730</span>
    <svg style="position:absolute;left:712px;top:2px" width="12" height="12" viewBox="0 0 24 24"><path d="M4 12a8 8 0 1 0 3-6" fill="none" stroke="#ccc" stroke-width="3"/><path d="M3 2v6h6" fill="#ccc"/></svg>
    <span style="left:741px">1 Monat Widerrufsrecht</span>
  </div>

  <header class="header">
    <div class="about">&#9432; Über uns &#8964;</div>
    <div class="logo"><div class="logo-name">FADENWELT<br>HÄNDLER</div><div class="logo-mark"></div></div>
    <div class="badge" style="left:511px;top:25px;width:44px;height:44px;background:#1da1d8"></div>
    <div class="badge" style="left:567px;top:31px;width:32px;height:32px;background:#e8b83a;border:3px solid #333"></div>
    <div class="badge" style="left:610px;top:34px;width:50px;height:26px;border-radius:4px;background:#cdd3dc"></div>
    <div class="badge" style="left:671px;top:31px;width:32px;height:32px;background:#1c4a8c"></div>
    <div class="search">Suchbegriff...
      <svg width="14" height="14" viewBox="0 0 24 24"><circle cx="10" cy="10" r="7" fill="none" stroke="#d2131d" stroke-width="3"/><path d="M15 15l7 7" stroke="#d2131d" stroke-width="3"/></svg>
    </div>
    <div class="btn" style="left:811px;width:26px"><svg width="13" height="12" viewBox="0 0 24 22"><path d="M12 21L2 11a6 6 0 0 1 10-8 6 6 0 0 1 10 8z" fill="#555"/></svg></div>
    <div class="btn" style="left:843px;width:77px"><svg width="12" height="12" viewBox="0 0 24 24"><circle cx="12" cy="7" r="6" fill="#555"/><path d="M0 24c0-8 24-8 24 0z" fill="#555"/></svg>Mein Konto</div>
    <div class="btn" style="left:923px;width:70px;color:var(--red);font-weight:700"><svg width="16" height="12" viewBox="0 0 28 22"><path d="M0 2h5l4 13h15l3-10H8" fill="none" stroke="#555" stroke-width="3"/><circle cx="11" cy="19" r="2.5" fill="#555"/><circle cx="22" cy="19" r="2.5" fill="#555"/></svg>&nbsp;0,00 € *</div>
  </header>

  <nav class="nav">
    <span class="home">Home</span>
    <span style="left:262px">Nähmaschinen</span>
    <span style="left:349px">Stickmaschinen</span>
    <span style="left:439px">Overlock</span>
    <span style="left:498px">Coverlock</span>
    <span style="left:561px">Sticksoftware</span>
    <span style="left:641px">Angebote</span>
    <span style="left:704px">Zubehör</span>
    <span style="left:761px">Zubehör nach Modell</span>
  </nav>

  <section class="hero">
    <div class="hero-title">WILDE STOFF TAGE</div>
    <div class="hero-date">GÜLTIG VON 21. - 28.11.2022</div>
    <svg class="ribbon" width="216" height="252" viewBox="0 0 216 252">
      <path d="M0 0H216V251L108 221L0 251Z" fill="#c8151b"/>
      <path d="M11 10H205V234L108 212L11 234Z" fill="none" stroke="#fff" stroke-width="1.6" stroke-dasharray="6 4"/>
      <text x="108" y="57" text-anchor="middle" font-family="Bebas Neue, sans-serif" font-size="40" fill="#fff">BIS ZU</text>
      <text x="108" y="153" text-anchor="middle" font-family="Bebas Neue, sans-serif" font-size="120" fill="#fff">40%</text>
      <text x="108" y="192" text-anchor="middle" font-family="Bebas Neue, sans-serif" font-size="40" fill="#fff">SPAREN</text>
    </svg>
  </section>

  <section class="intro">
    <h1>Nähmaschinen Onlineshop mit professioneller Beratung</h1>
    <p>Die persönliche Beratung steht bei uns an oberster Stelle. Sollten Sie Fragen zu Ihrem bestehenden Modell, der Auswahl einer neuen Maschine oder beispielsweise dem Kauf des passenden Zubehörs haben, stehen wir Ihnen jederzeit beratend per Telefon oder E-Mail zur Verfügung.</p>
  </section>

  <div class="tile" style="left:195px;width:402px;background:linear-gradient(135deg,#c9474f,#e0787c 60%,#d65a62)" role="img" aria-label="Stoffe und Nähzubehör in Rottönen">
    <div class="tile-label" style="left:215px;width:187px">ZUBEHÖR</div>
  </div>
  <div class="tile" style="left:597px;width:402px;background:linear-gradient(90deg,#ececec,#f4f4f4)" role="img" aria-label="Rote Nähmaschine im Angebot">
    <div style="position:absolute;left:82px;top:12px;width:120px;height:50px;background:linear-gradient(180deg,#c4232c,#e6e6e6)"></div>
    <div class="tile-label" style="left:216px;width:186px">ANGEBOTE</div>
  </div>

  <div class="cookie">
    <p>Diese Website benutzt Cookies, die für den technischen Betrieb der Website erforderlich sind und stets gesetzt werden. Andere Cookies, die den Komfort bei Benutzung dieser Website erhöhen, der Direktwerbung dienen oder die Interaktion mit anderen Websites und sozialen Netzwerken vereinfachen sollen, werden nur mit Ihrer Zustimmung gesetzt. <a href="#">Mehr Informationen</a></p>
    <div class="cbtn" style="left:962px;width:55px">Ablehnen</div>
    <div class="cbtn" style="left:1023px;width:85px">Alle akzeptieren</div>
    <div class="cbtn primary" style="left:1113px;width:75px">Konfigurieren</div>
  </div>

  <aside class="trust">
    <div class="seal"></div>
    <div>Käuferschutz</div>
    <div class="stars">★★★★★</div>
    <div style="font-weight:700;font-size:8px">4,91</div>
    <div>Sehr gut</div>
  </aside>

</div>
</body>
</html>
```